Business Card Design for an Investment Company

We need a business card design for our private investment company, called Ashbourne Partners. Ashbourne Partners is an investments partnership that aims to acquire shares in listed companies with a view to influencing those companies through active dialogue in order to improve their value. We need designs that use the logo colors (blue, grey, white), we need both English and Arabic on the business cards (can be on one side or 2 sides). The final logo should communicate professionalism, conservatism (nothing too fancy or too cheesy), that we are smart, conservative and old school.

Target Market(s)

Investment companies

Industry/Entity Type

Investment

Contact Information for Business Card

Khalid Yousef Rumaithi
Senior Executive Officer

Palm Terrace 07, Level 3, Office 215/12
HLMZ

+9714987650
krumaithi@ashbournepartners.com
www.ashbournepartners.com

Requirements
Must have
• Logo to be placed on the left hand side of the business card
• for the Arabic, we only need to have the name and title so it can be accomodated on one side so we can have the other side with full color and logo. The arabic that needs to be used is the below:
• خالد يوسف الرميثي
• المدير التنفيدي

```html
<!DOCTYPE html>
<html lang="en">
<head>
<meta charset="utf-8">
<title>Ashbourne Partners — Business Card</title>
<link href="https://fonts.googleapis.com/css2?family=Open+Sans:wght@400;600;700&family=Noto+Kufi+Arabic:wght@400;600&display=swap" rel="stylesheet">
<style>
  :root {
    --backdrop: #0e0e0e;
    --card: #231f20;
    --blue: #1a6ea8;
    --grey: #5a5a5c;
    --text-light: #c9c9c9;
    --white: #ffffff;
  }
  * { margin: 0; padding: 0; box-sizing: border-box; }
  html, body {
    width: 1200px; height: 844px; overflow: hidden;
    background: var(--backdrop);
    font-family: "Open Sans", Arial, sans-serif;
  }
  .stage {
    position: relative; width: 1200px; height: 844px;
    display: flex; align-items: center; justify-content: center; gap: 60px;
  }
  .card {
    position: relative; width: 520px; height: 300px;
    background: var(--card);
    box-shadow: 0 10px 30px rgba(0,0,0,.6);
    overflow: hidden;
  }
  .wordmark {
    display: flex; align-items: center; gap: 10px;
    color: var(--white); font-weight: 700; letter-spacing: -0.5px;
    white-space: nowrap;
  }
  .wordmark__square { background: var(--grey); flex: none; }

  /* Front */
  .card--front .wordmark {
    position: absolute; left: 40px; top: 50px; font-size: 32px;
  }
  .card--front .wordmark__square { width: 24px; height: 24px; }
  .contact {
    position: absolute; left: 222px; top: 116px;
    color: var(--text-light); font-size: 12.5px; line-height: 1.4;
    white-space: nowrap;
  }
  .contact__name { color: var(--blue); font-weight: 600; font-size: 14px; }
  .contact__title { margin-bottom: 12px; }
  .contact__row { display: flex; align-items: center; gap: 7px; }
  .contact__row svg { width: 10px; height: 10px; fill: var(--blue); flex: none; }
  .contact__address { margin-top: 12px; }

  /* Back */
  .card--back .wordmark {
    position: absolute; left: 50%; top: 50%;
    transform: translate(-50%, -50%); font-size: 34px;
  }
  .card--back .wordmark__square { width: 26px; height: 26px; }
  .arabic {
    position: absolute; right: 32px; bottom: 26px; text-align: right;
    direction: rtl; color: var(--text-light);
    font-family: "Noto Kufi Arabic", "Open Sans", sans-serif;
    font-size: 12px; line-height: 1.6;
  }
  .arabic__name { color: var(--blue); font-weight: 600; font-size: 14px; }
</style>
</head>
<body>
<main class="stage">
  <section class="card card--front">
    <div class="wordmark"><span class="wordmark__square"></span>Ashbourne Partners</div>
    <div class="contact">
      <div class="contact__name">Khalid Yousef Rumaithi</div>
      <div class="contact__title">Senior Executive Officer</div>
      <div class="contact__row">
        <svg viewBox="0 0 10 10" aria-hidden="true"><path d="M2 0.5 L3.6 0.5 L4.2 2.8 L3.1 3.6 Q4 5.9 6.4 6.9 L7.2 5.8 L9.5 6.4 L9.5 8 Q9.5 9.5 8 9.5 Q0.5 8.8 0.5 2 Q0.5 0.5 2 0.5 Z"/></svg>
        <span>+9714987650</span>
      </div>
      <div class="contact__row">
        <svg viewBox="0 0 10 10" aria-hidden="true"><path d="M0.5 2 H9.5 V8.5 H0.5 Z M0.5 2 L5 5.6 L9.5 2" stroke="#231f20" stroke-width="0.8"/></svg>
        <span>krumaithi@ashbournepartners.com</span>
      </div>
      <div class="contact__row">
        <svg viewBox="0 0 10 10" aria-hidden="true"><circle cx="5" cy="5" r="4.6"/><path d="M0.6 5 H9.4 M5 0.4 V9.6 M5 0.5 Q2.3 5 5 9.5 M5 0.5 Q7.7 5 5 9.5" stroke="#231f20" stroke-width="0.6" fill="none"/></svg>
        <span>www.ashbournepartners.com</span>
      </div>
      <div class="contact__address">Palm Terrace 07, Level 3, Office 215/12<br>HLMZ</div>
    </div>
  </section>

  <section class="card card--back">
    <div class="wordmark"><span class="wordmark__square"></span>Ashbourne Partners</div>
    <div class="arabic" lang="ar">
      <div class="arabic__name">خالد يوسف الرميثي</div>
      <div class="arabic__title">المدير التنفيدي</div>
    </div>
  </section>
</main>
</body>
</html>
```